Vex

I have the logo for the back already. Need the front to match.
Need a VEX logo which I can provide or you can download one - VEX Realty in canada... Back of the card will be my logo and name. Front will have the info...
I would like a black background. Match colors on front to the back..
Details on Card

Target Market(s)

Realestate clients.. Keep it classy like the logo

Contact Information for Business Card

Moren Tadwick office - 5817730264 cell - 5819063147 email - Moren@MorenTadwick.Com. website - MorenTadwick.Com Facebook - MTadwRealty Instagram - Moren_Qpl_Realtor Address - 418 - 23 St NE | K5P2M8

Colors
3176b5
33a6d7
85cae6

Requirements
Must have
• same color scheme as the logo
logo will be on the back
Black Background
Horizontal card
The one side of the card should be clean. like I stated, just my logo " Moren Tadwick " and nothing else

```html
<!DOCTYPE html>
<html lang="en">
<head>
<meta charset="utf-8">
<title>Moren Tadwick – Business Card</title>
<link href="https://fonts.googleapis.com/css2?family=Cinzel:wght@600&family=Open+Sans:wght@400;600&display=swap" rel="stylesheet">
<style>
  :root{
    --bg:#e6ecee;
    --card-dark:#2a2c30;
    --card-light:#ffffff;
    --blue-deep:#3176b5;
    --blue:#33a6d7;
    --blue-light:#85cae6;
    --ink:#4a4f55;
    --ink-soft:#9aa0a6;
  }
  *{margin:0;padding:0;box-sizing:border-box}
  html,body{width:717px;height:1200px;overflow:hidden}
  body{background:var(--bg);font-family:"Open Sans",sans-serif;position:relative}
  .card{position:absolute;left:78px;width:560px;height:320px;border-radius:16px;overflow:hidden;box-shadow:0 6px 18px rgba(0,0,0,.18)}
  .card--back{top:230px;background:var(--card-dark)}
  .card--front{top:640px;background:var(--card-light)}
  .bands{position:absolute;inset:0}

  /* back */
  .back-name{position:absolute;top:128px;left:0;right:0;text-align:center;font-family:"Cinzel",serif;font-weight:600;font-size:32px;line-height:40px;color:var(--blue);letter-spacing:2px}
  .back-web{position:absolute;top:270px;left:0;right:0;text-align:center;font-size:11px;line-height:16px;color:#9ba3aa}

  /* front */
  .identity{position:absolute;left:40px;top:40px}
  .name{font-family:"Cinzel",serif;font-weight:600;font-size:27px;color:var(--blue-deep);letter-spacing:1px}
  .role{font-size:11px;color:var(--ink-soft);margin-top:2px}
  .contacts{position:absolute;left:40px;top:114px;list-style:none}
  .contacts li{display:flex;align-items:center;gap:12px;font-size:12px;color:var(--ink);height:28px}
  .icon{width:18px;height:18px;border-radius:3px;background:var(--blue-deep);display:flex;align-items:center;justify-content:center;flex:none}
  .brand{position:absolute;right:40px;top:44px;display:flex;align-items:center;gap:8px}
  .brand-mark{width:18px;height:18px;background:var(--blue-deep)}
  .brand-name{font-weight:600;font-size:18px;color:var(--blue-deep)}
  .website{position:absolute;right:40px;top:212px;display:flex;align-items:center;gap:10px;font-size:12px;color:var(--ink)}
  .social{position:absolute;left:0;bottom:22px;height:30px;width:100%;display:flex;align-items:center;gap:30px;padding-left:40px;font-size:11px;color:#fff}
  .social span{display:flex;align-items:center;gap:8px}
  .social .sq{width:16px;height:16px;border-radius:3px;background:#fff;opacity:.9}
</style>
</head>
<body>

<section class="card card--back" aria-label="Card back">
  <svg class="bands" viewBox="0 0 560 320" aria-hidden="true">
    <polygon points="0,40 70,40 50,58 0,58" fill="var(--blue-deep)"/>
    <polygon points="560,40 490,40 510,58 560,58" fill="var(--blue-deep)"/>
    <polygon points="0,236 200,236 180,256 0,256" fill="var(--blue)"/>
    <polygon points="205,236 240,236 220,256 185,256" fill="var(--blue-light)"/>
    <polygon points="560,236 360,236 380,256 560,256" fill="var(--blue)"/>
    <polygon points="355,236 320,236 340,256 375,256" fill="var(--blue-light)"/>
  </svg>
  <div class="back-name">MOREN TADWICK</div>
  <div class="back-web">MorenTadwick.Com</div>
</section>

<section class="card card--front" aria-label="Card front">
  <svg class="bands" viewBox="0 0 560 320" aria-hidden="true">
    <polygon points="0,268 330,268 310,298 0,298" fill="var(--blue-deep)"/>
    <polygon points="335,268 560,268 560,298 315,298" fill="var(--blue-light)"/>
    <polygon points="320,268 370,268 350,298 300,298" fill="var(--blue)"/>
  </svg>

  <div class="identity">
    <div class="name">MOREN TADWICK</div>
    <div class="role">Real Estate Agent</div>
  </div>

  <div class="brand"><span class="brand-mark"></span><span class="brand-name">VEX Realty</span></div>

  <ul class="contacts">
    <li><span class="icon"><svg width="10" height="10" viewBox="0 0 10 10"><path d="M2 1l2 2-1 1.2c.6 1.2 1.6 2.2 2.8 2.8L7 6l2 2-1.2 1.2C4.5 9 1 5.5.8 2.2z" fill="#fff"/></svg></span>581-773-0264</li>
    <li><span class="icon"><svg width="10" height="10" viewBox="0 0 10 10"><rect x="2.5" y="0.5" width="5" height="9" rx="1" fill="#fff"/></svg></span>581-906-3147</li>
    <li><span class="icon"><svg width="10" height="10" viewBox="0 0 10 10"><path d="M5 0a3.3 3.3 0 0 1 3.3 3.3C8.3 6 5 10 5 10S1.7 6 1.7 3.3A3.3 3.3 0 0 1 5 0z" fill="#fff"/><circle cx="5" cy="3.3" r="1.2" fill="var(--blue-deep)"/></svg></span>418 - 23 St NE | K5P2M8</li>
    <li><span class="icon"><svg width="10" height="10" viewBox="0 0 10 10"><rect x="0.5" y="2" width="9" height="6" fill="#fff"/><path d="M0.5 2L5 5.5 9.5 2" stroke="var(--blue-deep)" fill="none"/></svg></span>Moren@MorenTadwick.Com</li>
  </ul>

  <div class="website"><span class="icon"><svg width="10" height="10" viewBox="0 0 10 10"><circle cx="5" cy="5" r="4" stroke="#fff" fill="none"/><path d="M1 5h8M5 1c-2 2.5-2 5.5 0 8M5 1c2 2.5 2 5.5 0 8" stroke="#fff" fill="none" stroke-width=".8"/></svg></span>MorenTadwick.Com</div>

  <div class="social">
    <span><i class="sq"></i>MTadwRealty</span>
    <span><i class="sq"></i>Moren_Qpl_Realtor</span>
  </div>
</section>

</body>
</html>
```